Velmora Construction Company Catalogue Design Project

looking for construction company catalog design, elegant, modern and shick

i made the project guaranteed for payment, waiting for serious designers. 

Reason: just made the project payment guaranteed/ so i am extending the deadline for another week.

Target Market(s)

ages 35 to 70 married couples

Industry/Entity Type

Construction

Requirements
Must have
• it should not look tacky with bunch of colors with cheesy layouts.

modern elegant shick page layout, construction company catalog showing company info and previous reference projects.

the catalog will be bound to 8.5x11" letter paper (or A4 europe)

the company info can be reached at http://www.velmora-example.com.tr/English/

```html
<!DOCTYPE html>
<html lang="en">
<head>
<meta charset="utf-8">
<title>Velmora Construction Company – Catalogue</title>
<link rel="stylesheet" href="https://fonts.googleapis.com/css2?family=Oswald:wght@300;400&family=Open+Sans:wght@300;400;600&display=swap">
<style>
  :root{
    --backdrop:#3b3b3b;
    --paper:#ffffff;
    --paper-grey:#dcdcdc;
    --accent:#c8262c;
    --accent-deep:#a0242a;
    --ink:#3a3a3a;
    --ink-soft:#8a8a8a;
    --brand:#2b7a9a;
    --brand-dot:#7cb342;
  }
  *{box-sizing:border-box;margin:0;padding:0}
  html,body{width:1200px;height:1000px;overflow:hidden}
  body{background:var(--backdrop);font-family:"Open Sans",sans-serif;color:var(--ink);position:relative}

  .spread{position:absolute;background:var(--paper);box-shadow:0 6px 18px rgba(0,0,0,.45);overflow:hidden}
  .page{position:absolute;top:0;bottom:0}
  .page--grey{background:radial-gradient(ellipse at 55% 40%,#ffffff 0%,#efefef 45%,var(--paper-grey) 100%)}
  .photo{position:absolute}

  .heading{font-family:"Oswald",sans-serif;font-weight:300;color:var(--accent);position:absolute;white-space:nowrap;letter-spacing:.2px}
  .heading--large{font-size:15px}
  .heading--small{font-size:11.5px}
  .heading .bar{display:inline-block;width:2px;height:.85em;background:var(--accent);vertical-align:-1px}
  .body-copy{position:absolute;font-size:4.6px;line-height:6.4px;color:var(--ink)}
  .body-copy p{margin-bottom:5px}

  /* spread 1 */
  .spread--about{left:90px;top:80px;width:493px;height:348px}
  .about-photo{left:0;top:0;width:245px;height:348px;background:linear-gradient(160deg,#8ea3c6 0%,#5d6f92 35%,#3d3a36 60%,#6b4a30 80%,#2a2622 100%)}
  .about-page{left:245px;width:248px}

  /* spread 2 */
  .spread--project{left:670px;top:80px;width:496px;height:350px}
  .project-photo{left:0;top:0;width:496px;height:272px;background:linear-gradient(180deg,#2f7fd0 0%,#7fb6e6 35%,#c9d7d8 52%,#6f9a5a 70%,#3f7d58 85%,#5aa9b0 100%)}
  .project-band{position:absolute;left:0;top:272px;width:496px;height:78px;background:var(--paper)}
  .project-band .divider{position:absolute;left:248px;top:6px;bottom:6px;width:1px;background:#e6e6e6}
  .brand{position:absolute;left:32px;top:30px;display:flex;align-items:center;gap:4px;font-size:10px;color:var(--brand);font-weight:600}
  .brand .dot{width:7px;height:7px;border-radius:50%;background:var(--brand-dot)}
  .project-title{position:absolute;left:102px;top:30px;font-weight:300;font-size:12px;letter-spacing:.6px;color:var(--ink-soft)}
  .project-facts{position:absolute;left:322px;top:14px;font-size:4.8px;line-height:10px;color:var(--ink-soft)}

  /* spread 3 */
  .spread--services{left:90px;top:513px;width:495px;height:350px}
  .services-left{left:0;width:248px;background:var(--paper)}
  .services-right{left:248px;width:247px}
  .service-list{position:absolute;left:34px;top:90px;list-style:none;font-size:5.2px;line-height:9.6px;color:var(--ink)}
  .circle-photo{position:absolute;border-radius:50%;border:2px solid #fff}
  .circle-office{left:32px;top:182px;width:146px;height:142px;background:radial-gradient(circle at 55% 65%,#e8c48c 0%,#c58b52 40%,#8a8f98 75%,#c7ccd2 100%)}
  .circle-plans{left:141px;top:166px;width:80px;height:78px;background:radial-gradient(circle at 40% 30%,#f1c232 0%,#b9c8dc 40%,#6a88b4 100%)}
  .circle-tower{left:336px;top:256px;width:66px;height:66px;background:linear-gradient(180deg,#7fa6d6 0%,#b8c0c8 45%,#6d6d6d 100%)}
  .refs-title{position:absolute;left:376px;top:104px;font-size:5px;font-weight:600}
  .refs{left:376px;top:114px;width:104px}

  /* spread 4 */
  .spread--interior{left:673px;top:512px;width:495px;height:350px}
  .interior-photo{left:0;top:0;width:248px;height:350px;background:linear-gradient(170deg,#2d6fd6 0%,#5b8fdc 30%,#c58b55 50%,#e2e2e2 70%,#8c6b4b 100%)}
  .interior-label{position:absolute;left:175px;top:78px;width:146px;height:86px;background:var(--accent-deep);opacity:.92;color:#fff;font-family:"Oswald",sans-serif;font-weight:300;font-size:29px;line-height:34px;letter-spacing:1px;padding:8px 0 0 80px}
  .thumb{position:absolute;left:385px;width:89px;height:60px}
  .thumb-1{top:31px;background:linear-gradient(135deg,#9a8468,#5c5147,#c9b79a)}
  .thumb-2{top:112px;background:linear-gradient(135deg,#e6e6e6,#8a8a8a,#d4d4d4)}
  .thumb-3{top:192px;background:linear-gradient(135deg,#cfcfcf,#4a3a30,#9a9a9a)}
  .thumb-4{top:274px;background:linear-gradient(135deg,#b8a07e,#e8e8e8,#f4f4f4)}
</style>
</head>
<body>

<section class="spread spread--about">
  <div class="photo about-photo" role="img" aria-label="Photograph of a modern residential building with wooden balconies and glass railings at dusk"></div>
  <div class="page page--grey about-page">
    <h2 class="heading heading--large" style="right:40px;top:66px">About Velmora <span class="bar"></span></h2>
    <div class="body-copy" style="left:34px;top:118px;width:176px">
      <p>Rapidly growing cities and changing lifestyles call for buildings that are safe, lasting and carefully planned for every family.</p>
      <p>In recent years our region has become one of the fastest growing markets in construction.</p>
      <p>Velmora was founded to follow this change with long experience in building and development.</p>
      <p>We deliver residential, commercial and public projects to international standards with skilled engineers.</p>
      <p>Our aim is to answer client needs with quality, speed and honest partnership.</p>
    </div>
  </div>
</section>

<section class="spread spread--project">
  <div class="photo project-photo" role="img" aria-label="Rendering of a residential complex with a tall tower, terraced green blocks and a landscaped canal park"></div>
  <div class="project-band">
    <div class="brand"><span class="dot"></span>lindera</div>
    <h2 class="project-title">LINDERA PARK</h2>
    <div class="divider"></div>
    <div class="project-facts">
      Client: Northvale REIT and Corvan Group<br>
      Block and lake works, fine finishes<br>
      Mechanical and decoration contracts<br>
      2010 - 2012
    </div>
  </div>
</section>

<section class="spread spread--services">
  <div class="page services-left">
    <h2 class="heading heading--small" style="left:32px;top:46px"><span class="bar"></span> OUR FIELDS OF WORK :</h2>
    <ul class="service-list">
      <li>Construction and Contracting</li>
      <li>Real Estate Development</li>
      <li>Urban Renewal and Restoration</li>
      <li>Project Management and Technical Consulting</li>
      <li>Building Consultancy</li>
      <li>Design</li>
    </ul>
    <div class="circle-photo circle-office" role="img" aria-label="Photograph of a bright office reception with a curved wooden desk"></div>
    <div class="circle-photo circle-plans" role="img" aria-label="Photograph of a hard hat resting on architectural plans"></div>
  </div>
  <div class="page page--grey services-right">
    <h2 class="heading heading--small" style="right:28px;top:46px">CONSTRUCTION and CONTRACTING <span class="bar"></span></h2>
  </div>
  <div class="body-copy" style="left:262px;top:118px;width:108px">
    <p>Our team has gathered more than twenty years of experience in general contracting at home and abroad.</p>
    <p>We apply universal standards from design to delivery with safety at every step.</p>
    <p>Quality and standards are never compromised.</p>
    <p>We follow new technologies to stay ahead in the industry.</p>
  </div>
  <div class="refs-title">Some of our references:</div>
  <div class="body-copy refs">
    Lindera Park Project – Istanbul – Northvale REIT<br>
    Bluewater 2010 Housing – Istanbul<br>
    Harbor Plaza Center – Baku<br>
    Seafront Residences – Baku<br>
    Kestrel Office Building – Kavacık<br>
    Ardent Factory and Offices<br>
    Culture Hall and Museum – Moscow<br>
    Steel Roof and Facade Cladding – Moscow
  </div>
  <div class="circle-photo circle-tower" role="img" aria-label="Photograph of a high-rise apartment block"></div>
</section>

<section class="spread spread--interior">
  <div class="photo interior-photo" role="img" aria-label="Photograph of residential towers with curved wooden balconies against a blue sky"></div>
  <div class="interior-label">INTE<br>RIOR</div>
  <div class="thumb thumb-1" role="img" aria-label="Photograph of a finished lobby interior"></div>
  <div class="thumb thumb-2" role="img" aria-label="Photograph of a finished kitchen interior"></div>
  <div class="thumb thumb-3" role="img" aria-label="Photograph of an empty living room with wooden floor"></div>
  <div class="thumb thumb-4" role="img" aria-label="Photograph of a finished bathroom with bathtub"></div>
</section>

</body>
</html>
```